SUMMIT GATHERING 2021. August 20th -22nd.

The Hosts of the conference: Grace Tabernacle-Pastors Ron n Della ( Picture with two persons)

Guest Minister: Bishop Lucinda Okotieno. (Cedar Ridge Awakening)

Venue:
Sealand Gateway Lodgeview. 4817 North 239th Avenue Seattle, WA 98174.

Conference times.
Friday August 20th 6pm-8:30pm
Saturday August 21st. 6pm-8:30pm

Sunday August 22nd 10am-1pm
“ CHURCH RENEWAL GATHERING”

5pm-7:30pm
TWOFOLD SURGE GATHERING.

Target Market(s)

18-55

Industry/Entity Type

Religious/ Entertainment.

Requirements
Must have
• A highlight of the Relaunch service on Sunday August 22nd 5pm-7:30pm.
Nice to have
• Excellent ideas….

```html
<!DOCTYPE html>
<html lang="en">
<head>
<meta charset="utf-8">
<title>Summit Gathering 2021</title>
<link rel="stylesheet" href="https://fonts.googleapis.com/css2?family=League+Spartan:wght@700;800&family=Jost:wght@400;500&family=Bodoni+Moda:wght@400;500&display=swap">
<style>
  :root {
    --purple: #6a2c91;
    --ink: #111111;
    --paper: #ffffff;
    --panel-top: #a98bcb;
    --panel-bottom: #b48a74;
    --photo-a: #3a2a2a;
    --photo-b: #d9cfc6;
    --head: "League Spartan", "Arial Black", sans-serif;
    --sans: "Jost", Arial, sans-serif;
    --serif: "Bodoni Moda", Georgia, serif;
  }
  * { margin: 0; padding: 0; box-sizing: border-box; }
  html, body { width: 848px; height: 1200px; overflow: hidden; background: var(--paper); }
  .flyer { position: relative; width: 848px; height: 1200px; background: var(--paper); }

  .paint-wash {
    position: absolute; left: 262px; top: 235px; width: 560px; height: 920px;
    background:
      radial-gradient(ellipse 30% 10% at 28% 3%, rgba(110,200,170,.7), transparent 70%),
      radial-gradient(ellipse 45% 14% at 55% 10%, rgba(170,215,235,.55), transparent 70%),
      radial-gradient(ellipse 50% 20% at 40% 22%, rgba(230,230,140,.75), transparent 70%),
      radial-gradient(ellipse 55% 25% at 45% 45%, rgba(245,185,110,.75), transparent 72%),
      radial-gradient(ellipse 40% 18% at 85% 50%, rgba(250,200,215,.45), transparent 70%),
      radial-gradient(ellipse 60% 25% at 50% 72%, rgba(250,220,90,.8), transparent 72%),
      radial-gradient(ellipse 50% 14% at 55% 92%, rgba(250,230,110,.6), transparent 70%);
  }
  .paint-wash-left {
    position: absolute; left: 26px; top: 800px; width: 260px; height: 400px;
    background:
      radial-gradient(ellipse 60% 35% at 60% 30%, rgba(250,225,100,.7), transparent 70%),
      radial-gradient(ellipse 40% 25% at 30% 80%, rgba(180,220,240,.5), transparent 70%);
  }

  .host-photo {
    position: absolute; left: 26px; top: 36px; width: 239px; height: 356px;
    background: linear-gradient(160deg, var(--photo-a), #6b5048 45%, var(--photo-b));
  }
  .host-panel {
    position: absolute; left: 26px; top: 392px; width: 239px; height: 411px;
    background: linear-gradient(180deg, var(--panel-top) 0%, #ad8ba6 55%, var(--panel-bottom) 100%);
    text-align: center; color: var(--paper);
  }
  .host-label { position: absolute; left: 0; right: 0; top: 14px; font: 400 17px var(--sans); color: var(--ink); }
  .host-names { position: absolute; left: 0; right: 0; top: 34px; font: 400 30px var(--serif); letter-spacing: 2px; }
  .guest-photo {
    position: absolute; left: 23px; top: 126px; width: 184px; height: 184px; border-radius: 50%;
    background: radial-gradient(circle at 50% 40%, #c9b39f, #4b4b4b 70%, #8e8e8e);
  }
  .guest-label { position: absolute; left: 0; right: 0; top: 316px; font: 400 17px var(--sans); color: var(--ink); }
  .guest-name { position: absolute; left: 0; right: 0; top: 341px; font: 400 13.5px var(--serif); line-height: 1.4; }

  .brand { position: absolute; left: 51px; top: 1015px; display: flex; align-items: center; gap: 12px; }
  .brand-mark { width: 40px; height: 40px; background: var(--ink); }
  .brand-name { font: 500 18px var(--sans); color: var(--ink); letter-spacing: 1px; }

  .title { position: absolute; left: 300px; width: 510px; text-align: center; }
  .title-main { top: 40px; font: 800 124px/1 var(--head); color: var(--purple); letter-spacing: 2px; }
  .title-sub { top: 146px; font: 800 47px/1 var(--head); color: var(--ink); }
  .title-dates { top: 200px; font: 400 33px/1 var(--sans); color: var(--purple); }

  .info { position: absolute; left: 351px; width: 400px; text-align: center; }
  .info h2 { font: 800 26px/1 var(--head); color: var(--purple); margin-bottom: 6px; }
  .info p { font: 400 20px/29px var(--serif); color: var(--ink); }
  .venue { top: 290px; }
  .times { top: 452px; }
  .surge { top: 1008px; }
  .surge h2 { font-size: 25px; }

  .renewal-ring { position: absolute; left: 362px; top: 604px; width: 366px; height: 366px; }
  .renewal { position: absolute; left: 362px; top: 688px; width: 366px; text-align: center; }
  .renewal h2 { font: 800 46px/50px var(--head); color: var(--ink); margin-bottom: 8px; }
  .renewal p { font: 400 20px/29px var(--serif); color: var(--ink); }
</style>
</head>
<body>
<main class="flyer">
  <div class="paint-wash" role="img" aria-label="Soft watercolour paint strokes in green, blue, orange and yellow"></div>
  <div class="paint-wash-left" role="img" aria-label="Soft yellow watercolour wash"></div>

  <div class="host-photo" role="img" aria-label="Photo of the host pastors Ron and Della"></div>
  <section class="host-panel">
    <p class="host-label">GRACE TABERNACLE PASTORS</p>
    <p class="host-names">Ron &amp; Della</p>
    <div class="guest-photo" role="img" aria-label="Portrait of guest minister Bishop Lucinda Okotieno"></div>
    <p class="guest-label">GUEST MINISTER</p>
    <p class="guest-name">Bishop Lucinda Okotieno.<br>(Cedar Ridge Awakening)</p>
  </section>

  <div class="brand">
    <span class="brand-mark"></span>
    <span class="brand-name">GRACE TABERNACLE</span>
  </div>

  <h1 class="title title-main">SUMMIT</h1>
  <p class="title title-sub">GATHERING 2021</p>
  <p class="title title-dates">AUGUST 20TH -22ND.</p>

  <section class="info venue">
    <h2>VENUE</h2>
    <p>Sealand Gateway Lodgeview. 4817<br>North 239th Avenue Seattle,<br>WA 98174.</p>
  </section>

  <section class="info times">
    <h2>CONFERENCE TIMES</h2>
    <p>Friday August 20th 6pm-8:30pm<br>Saturday August 21st.<br>6pm-8:30pm</p>
  </section>

  <svg class="renewal-ring" viewBox="0 0 366 366" aria-hidden="true">
    <circle cx="183" cy="183" r="181" fill="none" stroke="var(--purple)" stroke-width="1.5"/>
  </svg>
  <section class="renewal">
    <h2>CHURCH<br>RENEWAL<br>GATHERING</h2>
    <p>Sunday August 22nd<br>10am-1pm</p>
  </section>

  <section class="info surge">
    <h2>TWOFOLD SURGE GATHERING</h2>
    <p>Sunday August 22nd<br>5pm-7:30pm</p>
  </section>
</main>
</body>
</html>
```